Elegant Business Card with Logo and Picture

Please create a business card that has the Logo colors add Gold and turquoise / use the attached logo - I would like a beautiful Business Card - Please make sure it's printed on both sides / Picture can go on one side Logo other
www.velmorshine.example
614-372-0586
Lyn Odessa Ferwick
lynodessaf@quillpost.example
Life Coach
Vantrell Certified Teacher / Life Coach / Interior Designer
Transformational Retreats

Target Market(s)

Women Men General

Industry/Entity Type

Life Coaching

Contact Information for Business Card

www.velmorshine.example
614-372-0586
Lyn Odessa Ferwick
Life Coach
Vantrell Certified Teacher / Yoga Teacher / Interior Designer

Font styles to use
Serif
Decorative

Colors
33a6d6
e34197
ffc214

Requirements
Must have
• Quality Paper and touch /
Nice to have
• Beautiful Touch and feel
Should not have
• needs to be elegant

```html
<!DOCTYPE html>
<html lang="en">
<head>
<meta charset="utf-8">
<title>Velmor Shine Coaching – Business Card</title>
<link href="https://fonts.googleapis.com/css2?family=Cutive&family=Montserrat:wght@400&display=swap" rel="stylesheet">
<style>
  :root {
    --stage: #e9e6e1;
    --card: #0a0a0a;
    --ink: #ffffff;
    --accent: #e03aa2;
    --photo-light: #e4e4e4;
    --photo-mid: #c9b59a;
    --photo-warm: #d9a8a0;
  }
  * { margin: 0; padding: 0; box-sizing: border-box; }
  html, body { width: 1200px; height: 780px; overflow: hidden; background: var(--stage); }
  .stage {
    width: 1200px; height: 780px;
    display: flex; align-items: center; justify-content: center; gap: 40px;
  }
  .card {
    position: relative; width: 560px; height: 320px;
    background: var(--card); overflow: hidden;
    box-shadow: 0 10px 28px rgba(0,0,0,.25);
    color: var(--ink);
  }
  .card-front .portrait { position: absolute; left: 0; top: 0; }
  .brand-mark {
    display: inline-block; width: 44px; height: 44px;
    border: 4px solid var(--accent); border-radius: 50%;
  }
  .brand-name {
    font-family: "Cutive", serif; letter-spacing: 2px; text-transform: uppercase;
  }
  .brand-tag {
    font-family: "Cutive", serif; color: var(--accent);
    text-transform: uppercase; letter-spacing: 8px;
  }
  .front-info { position: absolute; left: 305px; top: 34px; right: 20px; }
  .front-info .brand-mark { margin-left: 70px; }
  .front-info .brand-name { font-size: 19px; margin-top: 10px; }
  .front-info .brand-tag { font-size: 9px; margin-top: 2px; padding-left: 40px; }
  .person-name {
    font-family: "Cutive", serif; font-size: 16px; letter-spacing: 1.5px;
    text-transform: uppercase; margin-top: 30px;
  }
  .person-role {
    font-family: "Montserrat", sans-serif; color: var(--accent); font-size: 14px; margin-top: 2px;
  }
  .contact-list { list-style: none; margin-top: 20px; }
  .contact-list li {
    display: flex; align-items: center; gap: 8px;
    font-family: "Montserrat", sans-serif; font-size: 13px; margin-bottom: 6px;
  }
  .contact-icon { width: 16px; height: 16px; flex: none; }
  .back-brand {
    position: absolute; left: 0; right: 0; top: 70px; text-align: center;
  }
  .back-brand .brand-mark { width: 64px; height: 64px; border-width: 5px; }
  .back-brand .brand-name { font-size: 30px; margin-top: 12px; letter-spacing: 3px; }
  .back-brand .brand-tag { font-size: 11px; margin-top: 4px; letter-spacing: 12px; }
  .credentials {
    position: absolute; left: 0; right: 0; bottom: 34px; text-align: center;
    font-family: "Cutive", serif; font-size: 11.5px; letter-spacing: 1px; text-transform: uppercase;
  }
</style>
</head>
<body>
<main class="stage">
  <section class="card card-front">
    <svg class="portrait" width="320" height="320" viewBox="0 0 320 320">
      <defs>
        <linearGradient id="portraitTone" x1="0" y1="0" x2="1" y2="1">
          <stop offset="0" stop-color="var(--photo-light)"/>
          <stop offset=".55" stop-color="var(--photo-mid)"/>
          <stop offset="1" stop-color="var(--photo-warm)"/>
        </linearGradient>
      </defs>
      <path d="M0,0 L200,0 Q305,160 200,320 L0,320 Z" fill="url(#portraitTone)" role="img" aria-label="Portrait photo of the life coach"/>
      <path class="accent-arc" d="M200,0 Q305,160 200,320 L222,320 Q330,160 222,0 Z" fill="var(--accent)"/>
    </svg>
    <div class="front-info">
      <span class="brand-mark"></span>
      <p class="brand-name">Velmor Shine</p>
      <p class="brand-tag">Coaching</p>
      <p class="person-name">Lyn Odessa Ferwick</p>
      <p class="person-role">Life Coach</p>
      <ul class="contact-list">
        <li>
          <svg class="contact-icon" viewBox="0 0 16 16"><circle cx="8" cy="8" r="8" fill="var(--accent)"/><rect x="5.5" y="3.5" width="5" height="9" rx="1" fill="none" stroke="#fff" stroke-width="1.2"/></svg>
          614-372-0586
        </li>
        <li>
          <svg class="contact-icon" viewBox="0 0 16 16"><circle cx="8" cy="8" r="8" fill="var(--accent)"/><circle cx="8" cy="8" r="4.5" fill="none" stroke="#fff" stroke-width="1.1"/><path d="M3.5 8h9M8 3.5v9" stroke="#fff" stroke-width="1"/></svg>
          www.velmorshine.example
        </li>
      </ul>
    </div>
  </section>

  <section class="card card-back">
    <div class="back-brand">
      <span class="brand-mark"></span>
      <p class="brand-name">Velmor Shine</p>
      <p class="brand-tag">Coaching</p>
    </div>
    <p class="credentials">Vantrell Certified Teacher / Yoga Teacher / Interior Designer</p>
  </section>
</main>
</body>
</html>
```